Business Intelligence/Analytics Technology Company Business Card

We are a higher-end enterprise software development company working with Retailer POS data to provide business intelligence and analytical services to fortune 500 companies.

I have an immediate need for a professional/thick/bold business card. The same design aspects will spiral into more media such as flyers/folders/etc...

Our website is www.brenvolq.com for our product.

I like "Clean" designs if that makes sense, not a lot of "stuff".

The uploaded files, the A logo with the box is the style we're leaning towards, but the A logo without the blue box is all good too... get creative.

Target Market(s)

Executives of large companies, down to VP level..

Industry/Entity Type

Software

Requirements
Must have
• I'm wanting a thick designer like business card.

I think we're going to change our logo to a more quillmesh 8 looking style... http://www.brenvolq.com/card.ai as an example of our current business card.

The winner will also have knowledge of where i can get these things printed.
Nice to have
• Blue-ish color scheme? I'm open to anything. Our Competition is Red, and another is Green. So we'll stick with the Blue.

```html
<!DOCTYPE html>
<html lang="en">
<head>
<meta charset="utf-8">
<title>Brenvolq Business Card</title>
<link rel="stylesheet" href="https://fonts.googleapis.com/css2?family=Mulish:wght@300;400;600;700;800&display=swap">
<style>
  :root {
    --brand-blue: #0a6cc8;
    --band-blue: #0668c4;
    --paper: #ffffff;
    --stage: #2e2e2e;
    --font: "Mulish", sans-serif;
  }
  * { margin: 0; padding: 0; box-sizing: border-box; }
  html, body { width: 1200px; height: 900px; overflow: hidden; }
  body { background: var(--stage); font-family: var(--font); position: relative; }

  .card {
    position: absolute;
    top: 308px;
    width: 513px;
    height: 285px;
    border-radius: 18px;
    overflow: hidden;
  }

  /* Front */
  .card-front { left: 73px; background: var(--brand-blue); }
  .card-front .brand-mark {
    position: absolute; left: 29px; top: 186px;
    width: 60px; height: 64px; background: var(--paper);
  }
  .card-front .brand-name {
    position: absolute; left: 111px; top: 200px;
    color: var(--paper); font-size: 30px; font-weight: 400;
    letter-spacing: 0.42em; line-height: 36px;
  }

  /* Back */
  .card-back { left: 616px; background: var(--paper); }
  .card-back .brand-mark {
    position: absolute; left: 91px; top: 28px;
    width: 58px; height: 64px; background: var(--brand-blue);
  }
  .card-back .brand-name {
    position: absolute; left: 28px; top: 106px;
    color: var(--brand-blue); font-size: 23px; font-weight: 400;
    letter-spacing: 0.38em; line-height: 28px;
  }
  .holder {
    position: absolute; right: 43px; top: 143px; text-align: right;
    color: var(--brand-blue); font-weight: 800;
  }
  .holder-name { font-size: 20px; line-height: 24px; }
  .holder-title { font-size: 15px; line-height: 20px; }

  .contact-band {
    position: absolute; left: 0; right: 0; top: 190px; bottom: 0;
    background: var(--band-blue); color: var(--paper);
    font-size: 12px; line-height: 14.6px;
  }
  .company { position: absolute; left: 43px; top: 10px; }
  .company-name { font-weight: 700; }
  .contact-lines { position: absolute; right: 43px; top: 10px; text-align: right; }
  .line { display: flex; align-items: center; gap: 5px; }
  .contact-lines .line { justify-content: flex-end; }
  .icon { width: 10px; height: 10px; flex: none; }
</style>
</head>
<body>

<section class="card card-front" aria-label="Card front">
  <span class="brand-mark"></span>
  <span class="brand-name">BRENVOLQ</span>
</section>

<section class="card card-back" aria-label="Card back">
  <span class="brand-mark"></span>
  <span class="brand-name">BRENVOLQ</span>

  <div class="holder">
    <div class="holder-name">Marten Quillby</div>
    <div class="holder-title">President</div>
  </div>

  <div class="contact-band">
    <div class="company">
      <div class="company-name">BRENVOLQ Technology Group, Inc</div>
      <div>48 Harlow Street</div>
      <div>Fenwick, New York 10987</div>
      <div class="line">
        <svg class="icon" viewBox="0 0 10 10" fill="none" stroke="#fff" stroke-width="1">
          <circle cx="5" cy="5" r="4.3"/><ellipse cx="5" cy="5" rx="1.8" ry="4.3"/><path d="M0.7 5h8.6M1.5 2.8h7M1.5 7.2h7"/>
        </svg>
        <span>www.brenvolq.com</span>
      </div>
    </div>

    <div class="contact-lines">
      <div class="line"><span>555 014 2210</span>
        <svg class="icon" viewBox="0 0 10 10" fill="none" stroke="#fff" stroke-width="1.1"><rect x="2.5" y="0.6" width="5" height="8.8" rx="0.8"/><path d="M4.3 8h1.4"/></svg>
      </div>
      <div class="line"><span>555 014 2211</span>
        <svg class="icon" viewBox="0 0 10 10"><circle cx="5" cy="5" r="4.6" fill="#fff"/><path d="M3.4 2.6l1.2 1.3-.7.8c.4.8 1 1.4 1.8 1.8l.8-.7 1.3 1.2-.9 1c-2.2-.4-4-2.2-4.4-4.4z" fill="#0668c4"/></svg>
      </div>
      <div class="line"><span>555 014 2212</span>
        <svg class="icon" viewBox="0 0 10 10" fill="#fff"><rect x="2.5" y="0.8" width="5" height="2.6"/><rect x="0.6" y="3.6" width="8.8" height="3.8" rx="0.6"/><rect x="2.5" y="6.4" width="5" height="2.8"/></svg>
      </div>
      <div class="line"><span>marten@brenvolq.com</span>
        <svg class="icon" viewBox="0 0 10 10"><rect x="0.5" y="2" width="9" height="6.4" fill="#fff"/><path d="M0.7 2.3L5 5.6l4.3-3.3" fill="none" stroke="#0668c4" stroke-width="0.9"/></svg>
      </div>
    </div>
  </div>
</section>

</body>
</html>
```